Vollo Activewear business card design

I need a business card designed for my activewear business. I would like to use the colours pink, purple white and blue. please see attached logo. please include (name) Rosalind Thwaite (phone) 0417285630 (email) rozzivollo@mailbrook.net (ABN) 51837264019 . please include - Free shipping on all orders over $100

Target Market(s)

female

Contact Information for Business Card

Colors

Designer to choose colors to be used in the design.

Requirements
Must have
• I need a business card designed for my activewear business. I would like to use the colours pink, purple white and blue. please see attached logo. please include (name) Rosalind Thwaite (phone) 0417285630 (email) rozzivollo@mailbrook.net (ABN) 51837264019 . please include - Free shipping on all orders over $100

```html
<!DOCTYPE html>
<html lang="en">
<head>
<meta charset="utf-8">
<title>Vollo Activewear business card</title>
<link href="https://fonts.googleapis.com/css2?family=Roboto:wght@400;500&display=swap" rel="stylesheet">
<style>
  :root {
    --canvas: #2a2a2c;
    --card-white: #ffffff;
    --purple: #9b1bb0;
    --pink: #c872a3;
    --pink-light: #d28bb4;
    --pink-pale: #f3dcea;
    --violet-pale: #e6d3ec;
    --text-light: #ffffff;
  }
  * { margin: 0; padding: 0; box-sizing: border-box; }
  html, body { width: 1200px; height: 801px; overflow: hidden; }
  body {
    background: var(--canvas);
    font-family: "Roboto", Arial, sans-serif;
    position: relative;
  }
  .card {
    position: absolute;
    top: 250px;
    width: 520px;
    height: 300px;
    overflow: hidden;
    box-shadow: 0 12px 30px rgba(0,0,0,.45);
  }
  .card-front { left: 50px; background: var(--card-white); }
  .card-back { left: 630px; background: var(--pink); }

  .front-shapes { position: absolute; inset: 0; width: 100%; height: 100%; }

  .brand {
    position: absolute;
    left: 40px;
    top: 46px;
    display: flex;
    align-items: center;
    gap: 12px;
  }
  .brand-mark {
    width: 30px; height: 30px;
    border-radius: 50%;
    background: var(--pink);
  }
  .brand-name {
    font-weight: 500;
    font-size: 36px;
    letter-spacing: 2px;
    color: var(--purple);
  }

  .contact {
    position: absolute;
    left: 26px;
    top: 186px;
    color: var(--text-light);
  }
  .contact-name { font-size: 21px; font-weight: 500; margin-bottom: 10px; }
  .contact-list { list-style: none; font-size: 13px; line-height: 17px; }
  .contact-list li { display: flex; align-items: center; gap: 7px; }
  .contact-list svg { width: 11px; height: 11px; fill: var(--text-light); flex: none; }
  .contact-abn { margin-top: 2px; }

  .back-pattern {
    position: absolute;
    inset: 0;
    background:
      radial-gradient(ellipse at 30% 30%, rgba(255,255,255,.10), rgba(255,255,255,0) 60%),
      linear-gradient(135deg, var(--pink-light), var(--pink) 70%);
  }
  .shipping-note {
    position: absolute;
    right: 26px;
    bottom: 26px;
    width: 150px;
    text-align: center;
    color: var(--text-light);
    font-size: 14px;
    line-height: 16px;
  }
</style>
</head>
<body>

<section class="card card-front" aria-label="Card front">
  <svg class="front-shapes" viewBox="0 0 520 300" aria-hidden="true">
    <defs>
      <linearGradient id="decorTone" x1="0" y1="0" x2="1" y2="1">
        <stop offset="0" stop-color="var(--pink-pale)"/>
        <stop offset="1" stop-color="var(--violet-pale)"/>
      </linearGradient>
    </defs>
    <path d="M0 172 H250 C290 172 300 200 300 240 V300 H0 Z" fill="var(--purple)"/>
  </svg>

  <svg class="front-shapes" viewBox="0 0 520 300" role="img" aria-label="Large decorative outline symbol in pink and violet">
    <path d="M312 300 V218 C312 178 340 152 380 152 H520 V300 Z" fill="url(#decorTone)"/>
  </svg>

  <div class="brand">
    <span class="brand-mark" aria-hidden="true"></span>
    <span class="brand-name">VOLLO</span>
  </div>

  <div class="contact">
    <p class="contact-name">Rosalind Thwaite</p>
    <ul class="contact-list">
      <li><svg viewBox="0 0 24 24"><path d="M6.6 10.8a15 15 0 0 0 6.6 6.6l2.2-2.2c.3-.3.7-.4 1-.2 1.1.4 2.3.6 3.6.6.6 0 1 .4 1 1V20c0 .6-.4 1-1 1A17 17 0 0 1 3 4c0-.6.4-1 1-1h3.5c.6 0 1 .4 1 1 0 1.3.2 2.5.6 3.6.1.3 0 .7-.2 1z"/></svg>0417285630</li>
      <li><svg viewBox="0 0 24 24"><path d="M2 5h20v14H2z M2 5l10 8 10-8"/></svg>rozzivollo@mailbrook.net</li>
      <li><svg viewBox="0 0 24 24"><circle cx="12" cy="12" r="10"/></svg>www.volloactive.net</li>
      <li class="contact-abn">ABN: 51837264019</li>
    </ul>
  </div>
</section>

<section class="card card-back" aria-label="Card back">
  <div class="back-pattern" role="img" aria-label="Faint repeating outline pattern over pink"></div>
  <p class="shipping-note">Free shipping on all orders over $100</p>
</section>

</body>
</html>
```